Store Fixture business needs a buisness card design

We are looking for a business card design for a store fixture company. "KL Shelf Outfitters" we help small businesses with their start up by providing fixtures required to display their products.
It should have a simple yet innovative design in the front, and a refined look to our company.
We would like our logo, to have one of our products "display cases, clothing rack, mannequins" integrated in the design. And the rest of it just a clean look, which gives our address, store hours, and contact number, etc.
The color scheme as seen in the samples can be changed as long as the goal is achieved.
Industry/Entity Type
Business
Contact Information for Business Card
KL Shelf Outfitters
4362 Marlow Ave.
San Antonio,TX 78299
www.klshelfoutfitters.example
klpo@klshelfoutfitter.example
(210) 555-0188
M-F: 9-6pm
Sat: 10-3pm

```html
<!DOCTYPE html>
<html lang="en">
<head>
<meta charset="utf-8">
<title>KL Shelf Outfitters – Business Card</title>
<link rel="stylesheet" href="https://fonts.googleapis.com/css2?family=Open+Sans:wght@400;600;700&display=swap">
<style>
  :root {
    --backdrop: #ece9e6;
    --card-white: #ffffff;
    --gold: #e1a91a;
    --gold-deep: #d29a17;
    --charcoal: #4b4c4e;
    --ink: #4a4a4a;
    --on-gold: #ffffff;
    --display-red: #a8321c;
    --display-chrome: #b9bcbf;
    --display-cream: #ece6dc;
    --display-wood: #b06a3a;
  }
  * { box-sizing: border-box; margin: 0; padding: 0; }
  html, body {
    width: 1200px; height: 900px; overflow: hidden;
    background: var(--backdrop);
    font-family: "Open Sans", Arial, sans-serif;
  }
  .canvas { position: relative; width: 1200px; height: 900px; }

  .card {
    position: absolute;
    background: var(--card-white);
    overflow: hidden;
    box-shadow: 0 6px 18px rgba(0,0,0,0.15);
  }
  .card--front { left: 78px; top: 35px; width: 588px; height: 362px; }
  .card--back  { left: 388px; top: 505px; width: 567px; height: 352px; }

  .card__bands { position: absolute; left: 0; top: 0; }

  .brand { position: absolute; display: flex; align-items: center; gap: 18px; }
  .brand__mark { width: 80px; height: 80px; background: var(--gold); border-radius: 6px; flex: none; }
  .brand__name {
    color: var(--ink); font-weight: 600; font-size: 27px;
    line-height: 1.12; letter-spacing: 2px; text-transform: uppercase;
  }
  .card--front .brand { left: 122px; top: 34px; }
  .card--back .brand { left: 136px; top: 50px; }

  .details { position: absolute; color: var(--on-gold); font-size: 15.5px; line-height: 24px; }
  .details--address { left: 33px; top: 226px; }
  .details__heading { font-weight: 700; font-size: 17px; margin-top: 12px; }

  .contact { position: absolute; right: 36px; top: 242px; color: var(--on-gold); font-size: 15.5px; }
  .contact__row { display: flex; align-items: center; justify-content: flex-end; gap: 10px; height: 25px; }
  .contact__icon { width: 13px; height: 13px; flex: none; }

  .products { position: absolute; left: 0; top: 186px; width: 100%; height: 120px; }
  .product { position: absolute; top: 0; height: 118px; }
  .product--showcase { left: 40px; width: 92px; background: linear-gradient(180deg, #c2452a, var(--display-red)); }
  .product--form { left: 178px; width: 82px; background: linear-gradient(180deg, var(--display-cream), #e3d3b6); }
  .product--rack { left: 290px; width: 90px; background: linear-gradient(180deg, #dfe1e3, var(--display-chrome)); }
  .product--counter { left: 422px; top: 26px; height: 80px; width: 118px; background: linear-gradient(180deg, #e4eef0 60%, var(--display-wood)); }
</style>
</head>
<body>
<div class="canvas">

  <section class="card card--front">
    <svg class="card__bands" width="588" height="362" viewBox="0 0 588 362" aria-hidden="true">
      <defs>
        <linearGradient id="goldFill" x1="0" y1="0" x2="0" y2="1">
          <stop offset="0" stop-color="#e6b020"/>
          <stop offset="1" stop-color="#d49b16"/>
        </linearGradient>
      </defs>
      <polygon points="0,186 404,186 386,210 0,210" fill="#4b4c4e"/>
      <polygon points="0,214 392,214 418,177 588,177 588,362 0,362" fill="url(#goldFill)"/>
    </svg>

    <div class="brand">
      <span class="brand__mark"></span>
      <span class="brand__name">KL Shelf<br>Outfitters</span>
    </div>

    <div class="details details--address">
      <p>4362 Marlow Ave.</p>
      <p>San Antonio,TX 78299</p>
      <p class="details__heading">Store Timings:</p>
      <p>M-F: 9-6pm &nbsp;|&nbsp; Sat: 10-3pm</p>
    </div>

    <div class="contact">
      <p class="contact__row">(210) 555-0188
        <svg class="contact__icon" viewBox="0 0 16 16" aria-hidden="true"><path fill="#fff" d="M3.6 1.2l2.3 2.6-1.3 2c.9 2 2.6 3.7 4.6 4.6l2-1.3 2.6 2.3-1.3 2.2C7 15.4.6 9 .8 2.5z"/></svg>
      </p>
      <p class="contact__row">klpo@klshelfoutfitter.example
        <svg class="contact__icon" viewBox="0 0 16 16" aria-hidden="true"><rect x="1" y="3" width="14" height="10" fill="#fff"/><path d="M1 3l7 6 7-6" fill="none" stroke="#d9a11a" stroke-width="1.4"/></svg>
      </p>
      <p class="contact__row">www.klshelfoutfitters.example
        <svg class="contact__icon" viewBox="0 0 16 16" aria-hidden="true"><circle cx="8" cy="8" r="7" fill="#fff"/><path d="M1 8h14M8 1c-3 3.5-3 10.5 0 14M8 1c3 3.5 3 10.5 0 14" fill="none" stroke="#d9a11a" stroke-width="1"/></svg>
      </p>
    </div>
  </section>

  <section class="card card--back">
    <div class="brand">
      <span class="brand__mark"></span>
      <span class="brand__name">KL Shelf<br>Outfitters</span>
    </div>

    <div class="products">
      <div class="product product--showcase" role="img" aria-label="Photo of a red wall display case with glass shelves"></div>
      <div class="product product--form" role="img" aria-label="Photo of a dress form on a wooden stand"></div>
      <div class="product product--rack" role="img" aria-label="Photo of a chrome rolling clothing rack"></div>
      <div class="product product--counter" role="img" aria-label="Photo of a glass showcase counter with wood base"></div>
    </div>
  </section>

</div>
</body>
</html>
```